Varden Ridge Concrete Pumping needs a logo design and is in the concrete industry

A creative design for this Varden Ridge Concrete Pumping business. Using a trailer mounted line pump, not a boom pump.
Colour to be used is orange and a mix of white or black writing.
Target Market(s)
General Public, anyone
Industry/Entity Type
Concrete
Contact Information for Business Card
Varden Ridge Concrete Pumping
Brennan Holloway
PO BOX 47
Tarnby VIC 3261
Phone: 0491552083
Email: Holloway@postwren.com.au
Colors
f37122
000000
ffffff
Requirements
Must have
- Details listed
Nice to have
- A great logo
Should not have
- anything silly

```html
<!DOCTYPE html>
<html lang="en">
<head>
<meta charset="utf-8">
<title>Varden Ridge Concrete Pumping – Business Card</title>
<link rel="stylesheet" href="https://fonts.googleapis.com/css2?family=Open+Sans:wght@400;600;700&display=swap">
<style>
  :root {
    --orange: #f37122;
    --black: #1a1a1a;
    --white: #ffffff;
    --backdrop: #e9e6e2;
  }
  * { margin: 0; padding: 0; box-sizing: border-box; }
  html, body {
    width: 1200px;
    height: 1000px;
    overflow: hidden;
    background: var(--backdrop);
    font-family: "Open Sans", sans-serif;
  }
  .business-card {
    position: absolute;
    left: 100px;
    top: 201px;
    width: 1000px;
    height: 598px;
    background: var(--white);
    box-shadow: 0 6px 22px rgba(0,0,0,0.18);
  }
  .brand {
    position: absolute;
    top: 150px;
    left: 0;
    width: 100%;
    text-align: center;
    color: var(--orange);
    font-weight: 700;
    font-size: 54px;
    line-height: 1.2;
    letter-spacing: 1px;
    text-transform: uppercase;
  }
  .holder-name {
    position: absolute;
    top: 390px;
    left: 0;
    width: 100%;
    text-align: center;
    color: var(--orange);
    font-weight: 700;
    font-size: 30px;
    line-height: 40px;
    letter-spacing: 0.5px;
    text-transform: uppercase;
  }
  .contact-row {
    position: absolute;
    top: 447px;
    left: 0;
    width: 100%;
    display: flex;
    justify-content: center;
    gap: 30px;
    color: var(--black);
    font-size: 24px;
    line-height: 34px;
  }
  .contact-item { display: flex; align-items: center; gap: 8px; }
  .contact-item svg { width: 22px; height: 22px; fill: var(--orange); }
  .address-band {
    position: absolute;
    top: 515px;
    left: 0;
    width: 100%;
    height: 46px;
    background: var(--orange);
    color: var(--white);
    font-weight: 600;
    font-size: 23px;
    letter-spacing: 1.5px;
    display: flex;
    align-items: center;
    justify-content: center;
  }
</style>
</head>
<body>
  <div class="business-card">
    <div class="brand">Varden Ridge<br>Concrete Pumping</div>

    <div class="holder-name">Brennan Holloway</div>

    <div class="contact-row">
      <span class="contact-item">
        <svg viewBox="0 0 24 24" aria-hidden="true"><path d="M6.6 10.8a15.1 15.1 0 0 0 6.6 6.6l2.2-2.2a1 1 0 0 1 1-.25 11.4 11.4 0 0 0 3.6.57 1 1 0 0 1 1 1V20a1 1 0 0 1-1 1A17 17 0 0 1 3 4a1 1 0 0 1 1-1h3.5a1 1 0 0 1 1 1c0 1.25.2 2.45.57 3.57a1 1 0 0 1-.25 1z"/></svg>
        0491552083
      </span>
      <span class="contact-item">
        <svg viewBox="0 0 24 24" aria-hidden="true"><path d="M3 5h18v14H3z M3 5l9 7 9-7" stroke="#fff" stroke-width="1.6"/></svg>
        Holloway@postwren.com.au
      </span>
    </div>

    <div class="address-band">PO BOX 47 Tarnby VIC 3261</div>
  </div>
</body>
</html>
```